Flyer für Friseurin
Zielgruppe
Friseurin für Damen und Herren
Aufgabenstellung
https://lenvirasalon.de
Bitte erstelle mir anhand der Daten von der Website einen angepassten Entwurf mit Neueröffnung und geben keine Preise an sondern die kunden sollen sich direkt eingeladen führen um persönlich vor Ort vorbei zuschauen.

```html
<!DOCTYPE html>
<html lang="de">
<head>
<meta charset="utf-8">
<title>Lenvira Hair &amp; Beauty Lounge – Große Eröffnung</title>
<link rel="stylesheet" href="https://fonts.googleapis.com/css2?family=Cinzel:wght@600;700;800&family=Great+Vibes&family=Montserrat:wght@800&family=Figtree:wght@400&display=swap">
<style>
  :root {
    --stage: #e4e4e4;
    --ink: #050505;
    --paper: #ffffff;
    --gold-1: #b8862b;
    --gold-2: #f5c518;
    --gold-3: #e8c46a;
    --rose: #e0a58a;
    --sage: #a6c68a;
    --olive: #6b7a55;
    --text: #ffffff;
  }
  * { margin: 0; padding: 0; box-sizing: border-box; }
  html, body { width: 1200px; height: 1117px; overflow: hidden; background: var(--stage); }
  .flyer {
    position: absolute; left: 270px; top: 93px;
    width: 659px; height: 931px;
    background: var(--paper);
    overflow: hidden;
    font-family: "Figtree", sans-serif;
    color: var(--text);
    box-shadow: 0 18px 40px rgba(0,0,0,.25);
  }
  .flyer__dark { position: absolute; inset: 0; width: 659px; height: 931px; }
  .hero-photo {
    position: absolute; left: 0; top: 0; width: 659px; height: 430px;
    background: radial-gradient(ellipse at 45% 35%, #3a3430 0%, #1b1917 45%, rgba(5,5,5,0) 80%),
                linear-gradient(180deg, #1e1c1a 0%, #0d0c0b 70%, rgba(5,5,5,0) 100%);
  }
  .confetti { position: absolute; border-radius: 50%; filter: blur(6px); opacity: .85;
    background: radial-gradient(circle, var(--gold-3) 0%, var(--gold-1) 55%, rgba(184,134,43,0) 75%); }
  .confetti--left { left: -10px; top: 0; width: 150px; height: 170px; }
  .confetti--right { left: 560px; top: 80px; width: 100px; height: 130px; }
  .frame { position: absolute; inset: 0; width: 659px; height: 931px; }
  .brand {
    position: absolute; left: 0; width: 659px; top: 48px; text-align: center;
    font-family: "Cinzel", serif; font-weight: 700; color: var(--gold-3);
  }
  .brand__name { font-size: 26px; letter-spacing: 1px; line-height: 30px; }
  .brand__sub { font-size: 10px; letter-spacing: 2px; line-height: 14px; }
  .headline-script {
    position: absolute; left: 0; width: 659px; top: 122px; text-align: center;
    font-family: "Great Vibes", cursive; font-size: 96px; line-height: 110px; color: var(--text);
    padding-left: 12px;
  }
  .headline-main {
    position: absolute; left: 0; width: 659px; top: 216px; text-align: center;
    font-family: "Montserrat", sans-serif; font-weight: 800; font-size: 78px; line-height: 90px;
    letter-spacing: -1px;
    background: linear-gradient(90deg, var(--gold-1) 0%, var(--gold-2) 30%, var(--gold-1) 55%, var(--gold-3) 80%, var(--gold-1) 100%);
    -webkit-background-clip: text; background-clip: text; color: transparent;
  }
  .salon-name {
    position: absolute; left: 0; width: 659px; top: 302px; text-align: center;
    font-family: "Cinzel", serif; font-weight: 700; font-size: 42px; line-height: 40px;
  }
  .tagline {
    position: absolute; left: 0; width: 659px; top: 386px; text-align: center;
    font-size: 15.5px; line-height: 18.5px;
  }
  .gallery { position: absolute; top: 439px; left: 76px; display: flex; gap: 10px; }
  .gallery__item { width: 162px; height: 126px; border: 1.5px solid var(--gold-2); padding: 4px; }
  .gallery__fill { width: 100%; height: 100%; }
  .fill--curls { background: linear-gradient(135deg, #f2ede8 0%, #c98a5a 50%, #a4643a 100%); }
  .fill--stylist { background: linear-gradient(135deg, #5d4a38 0%, #8a7764 50%, #3b342f 100%); }
  .fill--products { background: linear-gradient(135deg, #3a2a1c 0%, #c49466 55%, #6d4a2c 100%); }
  .feature { position: absolute; left: 98px; top: 582px; width: 235px; }
  .feature__title {
    font-family: "Cinzel", serif; font-weight: 700; font-size: 14.5px; line-height: 16.5px; color: var(--rose);
    margin-bottom: 4px;
  }
  .feature__text { font-size: 11.2px; line-height: 13.8px; margin-bottom: 13px; }
  .quote {
    position: absolute; left: 348px; top: 582px; width: 230px;
    font-family: "Cinzel", serif; font-weight: 700; font-size: 13.4px; line-height: 15.8px;
  }
  .cta {
    position: absolute; left: 348px; top: 700px;
    font-family: "Cinzel", serif; font-weight: 800; font-size: 29px; line-height: 29px; color: var(--sage);
  }
  .footer {
    position: absolute; left: 95px; top: 843px; height: 30px; width: 470px;
    display: flex; align-items: center; color: #111;
  }
  .footer__label { font-size: 11px; margin-right: 8px; }
  .footer__dot { width: 24px; height: 24px; border-radius: 50%; background: var(--olive); margin-right: 6px; }
  .footer__handle { font-family: "Cinzel", serif; font-weight: 700; font-size: 18px; margin-right: 14px; }
  .footer__web {
    background: var(--olive); color: var(--paper); border-radius: 15px;
    height: 30px; padding: 0 16px; display: flex; align-items: center;
    font-family: "Cinzel", serif; font-weight: 700; font-size: 19px;
  }
</style>
</head>
<body>
<main class="flyer">
  <svg class="flyer__dark" viewBox="0 0 659 931" aria-hidden="true">
    <path d="M0 0 H659 V792 Q330 852 0 792 Z" fill="#050505"/>
  </svg>
  <div class="hero-photo" role="img" aria-label="Dunkles Foto einer Friseurin bei der Arbeit im Salon"></div>
  <div class="confetti confetti--left" role="img" aria-label="Goldene Luftschlangen"></div>
  <div class="confetti confetti--right" role="img" aria-label="Goldene Luftschlangen"></div>

  <svg class="frame" viewBox="0 0 659 931" aria-hidden="true">
    <defs>
      <linearGradient id="gold" x1="0" y1="0" x2="1" y2="1">
        <stop offset="0" stop-color="#b8862b"/>
        <stop offset=".5" stop-color="#f5c518"/>
        <stop offset="1" stop-color="#e8c46a"/>
      </linearGradient>
    </defs>
    <path d="M170 26 H26 V904 H633 V26 H492" fill="none" stroke="url(#gold)" stroke-width="3"/>
    <path d="M160 40 H42 V891 H617 V40 H500" fill="none" stroke="url(#gold)" stroke-width="0.8"/>
    <path d="M88 807 Q330 830 572 807" fill="none" stroke="#e0a58a" stroke-width="2"/>
  </svg>

  <div class="brand">
    <div class="brand__name">Lenvira Hair</div>
    <div class="brand__sub">BEAUTY LOUNGE</div>
  </div>

  <h1 class="headline-script">Große</h1>
  <div class="headline-main">ERÖFFNUNG</div>
  <h2 class="salon-name">Lenvira Hair &amp;<br>Beauty Lounge</h2>
  <p class="tagline">Erleben Sie Schönheit und Stil in perfekter Harmonie. Unsere<br>Experten verwandeln Ihre Träume in Realität.</p>

  <div class="gallery">
    <div class="gallery__item"><div class="gallery__fill fill--curls" role="img" aria-label="Lange Locken werden mit dem Lockenstab gestylt"></div></div>
    <div class="gallery__item"><div class="gallery__fill fill--stylist" role="img" aria-label="Porträt der Friseurin im Salon vor Produktregal"></div></div>
    <div class="gallery__item"><div class="gallery__fill fill--products" role="img" aria-label="Haarpflegeprodukte im Regal"></div></div>
  </div>

  <section class="feature">
    <h3 class="feature__title">Moderne Ausstattung &amp;<br>Wohlfühlatmosphäre</h3>
    <p class="feature__text">In unserem modernen Salon in Lindenbach erwarten Sie hochwertige Ausstattung und eine entspannte Atmosphäre. Unser erfahrenes Team sorgt dafür, dass Sie sich rundum wohlfühlen.</p>
    <p class="feature__text">Von klassischen Haarschnitten bis hin zu modernen Colorationen und Extensions - wir bieten Ihnen das komplette Spektrum der Friseurkunst auf höchstem Niveau.</p>
  </section>

  <blockquote class="quote">"Mehr als nur Haare. Wir schaffen Momente der Schönheit und des Wohlgefühls, die Ihre Persönlichkeit strahlen lassen – mit Herz, Hand und Leidenschaft."</blockquote>
  <div class="cta">Ihr neuer<br>Look wartet</div>

  <footer class="footer">
    <span class="footer__label">Folgen Sie uns auf</span>
    <span class="footer__dot"></span>
    <span class="footer__handle">@LENVIRA.SALON</span>
    <span class="footer__web">LENVIRASALON.DE</span>
  </footer>
</main>
</body>
</html>
```